Banner for Vet Hospital 5m x 1.2m - Heat Stroke

Maplecourt Pet Hospital needs a Heat Stroke Banner for Summer.
The banner will be 5000mm long and 1200mm tall.

Our region has been hot this year and this summer is going to be extremely hot.
I want to warn people about heat stroke.
I want you to create a heat stroke banner that conveys the symptoms of heat stroke.

Pictures are better than words.
There should be IMAGES and WORDS that can be seen from the road 30m away and maybe some smaller words for people to read as they walk past.

Here are some of the signs of Heat Stroke:
- Panting which increases as heatstroke progresses
- Drooling, salivating
- Agitation, restlessness
- Very red or pale gums
- Bright red tongue
- Increased heart rate
- Breathing distress
- Vomiting Diarrhea (possibly with blood)
- Signs of mental confusion, delirium
- Dizziness, staggering
- Lethargy, weakness
- Muscle tremors
- Seizures
- Collapsing and lying down
- Little to no urine production
- Coma

I have attached characters that we often use in our advertising. They are optional.
I have done a mock up of the design I imagine. You could refine this design or make your own....or both.

Target Market(s)

Women aged 20 to 50.

Industry/Entity Type

Veterinary

Font styles to use
Sans Serif

Colors
fbed22
f78f20
ec1f27
ffffff

Requirements
Must have
• Heat Stroke Symtpms.
• Heat Stroke Warning.
• Summer theme.
Nice to have
• Bright colours.

```html
<!DOCTYPE html>
<html lang="en">
<head>
<meta charset="utf-8">
<title>Heat Stroke Banner – Maplecourt Pet Hospital</title>
<link rel="stylesheet" href="https://fonts.googleapis.com/css2?family=Anton&family=Oswald:wght@500;600;700&display=swap">
<style>
  :root {
    --page-bg: #eceef0;
    --banner-yellow: #fde98a;
    --warning-red: #c8202a;
    --ink: #1c1c1c;
    --zone-mild: #f6d51f;
    --zone-moderate: #f3b335;
    --zone-severe: #f39a1d;
    --zone-critical: #e8352b;
    --zone-divider: #e23a2c;
    --dial-white: #ffffff;
    --dial-shade: #d9d9d9;
    --needle: #3d3d3d;
    --banner-edge: #3a8fd0;
  }
  * { margin: 0; padding: 0; box-sizing: border-box; }
  html, body {
    width: 1200px;
    height: 900px;
    overflow: hidden;
    background: var(--page-bg);
  }
  .banner {
    position: absolute;
    left: 20px;
    top: 274px;
    width: 1160px;
    height: 352px;
    background: var(--banner-yellow);
    border-bottom: 3px solid var(--banner-edge);
    overflow: hidden;
  }
  .banner__headline {
    position: absolute;
    left: 46px;
    top: 108px;
    font-family: "Anton", "Oswald", sans-serif;
    font-size: 96px;
    line-height: 1;
    letter-spacing: 3px;
    color: var(--warning-red);
  }
  .banner__callout {
    position: absolute;
    left: 48px;
    top: 228px;
    font-family: "Oswald", sans-serif;
    font-weight: 500;
    font-size: 19px;
    color: var(--warning-red);
    white-space: nowrap;
  }
  .gauge {
    position: absolute;
    left: 0;
    top: 0;
    width: 1160px;
    height: 352px;
  }
  .gauge__label {
    font-family: "Oswald", sans-serif;
    text-anchor: middle;
    dominant-baseline: middle;
  }
  .gauge__label--stage { fill: var(--warning-red); font-weight: 700; font-size: 21px; }
  .gauge__label--signs { fill: var(--ink); font-weight: 600; font-size: 18px; }
</style>
</head>
<body>
  <section class="banner" aria-label="Heat stroke warning banner">
    <h1 class="banner__headline">HEAT STROKE</h1>
    <p class="banner__callout">If your dog has any of these symptoms call 02 65550172</p>

    <svg class="gauge" viewBox="0 0 1160 352" xmlns="http://www.w3.org/2000/svg">
      <defs>
        <radialGradient id="dial-face" cx="829" cy="352" r="110" gradientUnits="userSpaceOnUse">
          <stop offset="0.55" stop-color="var(--dial-white)"/>
          <stop offset="1" stop-color="var(--dial-shade)"/>
        </radialGradient>
      </defs>

      <!-- severity zones -->
      <path class="gauge__zone gauge__zone--mild" fill="var(--zone-mild)"
            d="M614 352 A215 215 0 0 1 677 200 L751.2 274.2 A110 110 0 0 0 719 352 Z"/>
      <path class="gauge__zone gauge__zone--moderate" fill="var(--zone-moderate)"
            d="M677 200 A215 215 0 0 1 829 137 L829 242 A110 110 0 0 0 751.2 274.2 Z"/>
      <path class="gauge__zone gauge__zone--severe" fill="var(--zone-severe)"
            d="M829 137 A215 215 0 0 1 981 200 L906.8 274.2 A110 110 0 0 0 829 242 Z"/>
      <path class="gauge__zone gauge__zone--critical" fill="var(--zone-critical)"
            d="M981 200 A215 215 0 0 1 1044 352 L939 352 A110 110 0 0 0 906.8 274.2 Z"/>

      <!-- zone dividers -->
      <g class="gauge__dividers" stroke="var(--zone-divider)" stroke-width="2">
        <line x1="751.2" y1="274.2" x2="642" y2="165"/>
        <line x1="829" y1="242" x2="829" y2="87"/>
        <line x1="906.8" y1="274.2" x2="1016" y2="165"/>
      </g>

      <!-- dog character placeholders -->
      <g role="img" aria-label="Cartoon dog drooling and panting">
        <circle cx="678" cy="290" r="32" fill="#e9b81a"/>
      </g>
      <g role="img" aria-label="Cartoon dog that has vomited">
        <circle cx="766" cy="203" r="32" fill="#e79a22"/>
      </g>
      <g role="img" aria-label="Cartoon dog trembling and struggling to breathe">
        <circle cx="892" cy="203" r="32" fill="#e0850f"/>
      </g>
      <g role="img" aria-label="Cartoon dog collapsed on the ground">
        <circle cx="980" cy="290" r="32" fill="#cf2a22"/>
      </g>

      <!-- dial -->
      <path class="gauge__dial" fill="url(#dial-face)" d="M719 352 A110 110 0 0 1 939 352 Z"/>
      <polygon class="gauge__needle" fill="var(--needle)" points="823,350 835,352 863,258 858,256"/>
      <path class="gauge__hub" fill="var(--needle)" d="M813 352 A16 16 0 0 1 845 352 Z"/>

      <!-- stage labels -->
      <text class="gauge__label gauge__label--stage" transform="translate(581 249) rotate(-67.5)">EXCESSIVE PANTING</text>
      <text class="gauge__label gauge__label--signs" transform="translate(605 259) rotate(-67.5)">DROOLING AGITATION</text>

      <text class="gauge__label gauge__label--stage" transform="translate(726 104) rotate(-22.5)">VOMITING</text>
      <text class="gauge__label gauge__label--signs" transform="translate(736 128) rotate(-22.5)">DIARREHA</text>

      <text class="gauge__label gauge__label--stage" transform="translate(932 104) rotate(22.5)">MUSCLE TREMORS</text>
      <text class="gauge__label gauge__label--signs" transform="translate(922 128) rotate(22.5)">BREATHING DISTRESS</text>

      <text class="gauge__label gauge__label--stage" transform="translate(1077 249) rotate(67.5)">COMA</text>
      <text class="gauge__label gauge__label--signs" transform="translate(1053 259) rotate(67.5)">COLLAPSE</text>
    </svg>
  </section>
</body>
</html>
```